Business Card Design for New Game Studio

We need a business card design. We are a new company developing innovative mobile and platform games.

I would like to see very innovative design thats brings out the company's goal and direction.

My Company's goal and direction is to "Change The Way We Play, Bring Joy And Excitement To Every Player"

Please do use our company logo which I have attached to be included in the design.

Please put in details for name, title, contacts etc ... be creative !!!

Reason: Company logo redesign. Awaiting it. Thanks

Hi all Please do wait for my updated company logo. Thanks

Reason: Still waiting on new company logo. Thanks all

Hi All Designers .... Sorry for the long wait... Please see the new file for my new company logo uploaded. Waiting to see all your creative design. Cheers

Hi All .... Please do not just mass send a whole bunch of similar designs .... Would like to see quality instead of quantity Cheers

Industry/Entity Type

Entertainment

```html
<!DOCTYPE html>
<html lang="en">
<head>
<meta charset="utf-8">
<title>Novaplay Studio – Business Card</title>
<link rel="stylesheet" href="https://fonts.googleapis.com/css2?family=Open+Sans:wght@400;600;700&display=swap">
<style>
  :root {
    --page: #e9e7e2;
    --card-dark: #3e3e41;
    --band-olive: #56633a;
    --lime: #c6dc28;
    --ink: #111111;
    --ink-soft: #45452f;
    --white: #ffffff;
  }
  * { margin: 0; padding: 0; box-sizing: border-box; }
  html, body { width: 1200px; height: 720px; overflow: hidden; }
  body {
    background: var(--page);
    font-family: "Open Sans", Arial, sans-serif;
    position: relative;
  }
  .card {
    position: absolute;
    top: 202px;
    width: 555px;
    height: 317px;
    overflow: hidden;
    box-shadow: 0 8px 24px rgba(0,0,0,.18);
  }
  .card--front { left: 30px; background: var(--card-dark); color: var(--white); }
  .card--back { left: 615px; background: var(--lime); color: var(--ink-soft); text-align: center; }

  .front__band {
    position: absolute;
    top: 34px; right: 0;
    width: 330px; height: 64px;
    background: var(--band-olive);
  }
  .front__holder {
    position: absolute;
    top: 52px; right: 60px;
    font-size: 17px;
  }
  .front__holder strong { font-weight: 700; }
  .front__holder span { font-size: 12px; }

  .brand {
    display: flex; align-items: center; gap: 10px;
    font-weight: 700;
  }
  .brand__dot { width: 16px; height: 16px; background: var(--lime); }
  .front__brand {
    position: absolute; left: 30px; top: 120px;
    color: var(--lime); font-size: 22px;
  }

  .contacts {
    position: absolute; left: 30px; top: 196px;
    list-style: none; font-size: 13px; line-height: 21px;
  }
  .contacts li { display: flex; align-items: center; gap: 8px; }
  .contacts svg { width: 13px; height: 13px; flex: none; }

  .back__brand {
    justify-content: center;
    margin-top: 78px;
    color: var(--ink); font-size: 40px;
  }
  .back__brand .brand__dot { width: 28px; height: 28px; background: var(--ink); }
  .back__tagline {
    margin-top: 46px;
    font-size: 19px; line-height: 24px;
  }
  .back__web {
    margin-top: 14px;
    font-size: 18px; letter-spacing: 1px;
  }
</style>
</head>
<body>

<section class="card card--front" aria-label="Card front">
  <div class="front__band"></div>
  <p class="front__holder"><strong>Your Name,</strong> <span>Title</span></p>

  <div class="brand front__brand"><span class="brand__dot"></span>Novaplay Studio</div>

  <ul class="contacts">
    <li>
      <svg viewBox="0 0 16 16"><circle cx="8" cy="8" r="8" fill="var(--lime)"/><path d="M5 4l2 0 1 2-1 1c.5 1 1 1.5 2 2l1-1 2 1v2c-4 0-7-3-7-7z" fill="var(--card-dark)"/></svg>
      012-345-6789
    </li>
    <li>
      <svg viewBox="0 0 16 16"><circle cx="8" cy="8" r="8" fill="var(--lime)"/><rect x="5.5" y="3.5" width="5" height="9" rx="1" fill="var(--card-dark)"/></svg>
      012-345-6789
    </li>
    <li>
      <svg viewBox="0 0 16 16"><circle cx="8" cy="8" r="8" fill="var(--lime)"/><rect x="4" y="5" width="8" height="6" fill="var(--card-dark)"/><path d="M4 5l4 3 4-3" stroke="var(--lime)" fill="none"/></svg>
      info@novaplaystudio.com
    </li>
    <li>
      <svg viewBox="0 0 16 16"><circle cx="8" cy="8" r="8" fill="var(--lime)"/><circle cx="8" cy="8" r="4.5" fill="none" stroke="var(--card-dark)"/><path d="M3.5 8h9M8 3.5c-2 2.5-2 6.5 0 9M8 3.5c2 2.5 2 6.5 0 9" stroke="var(--card-dark)" fill="none" stroke-width=".8"/></svg>
      www.novaplaystudio.com
    </li>
    <li>
      <svg viewBox="0 0 16 16"><circle cx="8" cy="8" r="8" fill="var(--lime)"/><path d="M8 3a3 3 0 0 1 3 3c0 2.5-3 6-3 6s-3-3.5-3-6a3 3 0 0 1 3-3z" fill="var(--card-dark)"/><circle cx="8" cy="6" r="1" fill="var(--lime)"/></svg>
      Street Name, City Name, Zip Code - 000000
    </li>
  </ul>
</section>

<section class="card card--back" aria-label="Card back">
  <div class="brand back__brand"><span class="brand__dot"></span>Novaplay Studio</div>
  <p class="back__tagline">Change The Way We Play, Bring Joy And<br>Excitement To Every Player</p>
  <p class="back__web">www.novaplaystudio.com</p>
</section>

</body>
</html>
```